BQL Groundworks & Freight Business Card

Can you please design a business card for an Earthworks, Haulage truck and machinery hire company. They also provide sand soil and mulch supply, as well as screening of products. Can you re-create the logo from the attached but add BQL Groundworks & Freight just use the three diamond design.

Target Market(s)

Earthmoving and Transport, Landscapers, Construction

Contact Information for Business Card

ABN 52 907 334 816, Doug Pelham, Managing Director, BQL Groundworks & Freight Mobile 0438 256 904 Email bqlfreight2010@mailvane.net

Font styles to use
Sans Serif

Colors
ec1f27
000000
cbcbcb
ffffff

Requirements
Must have
• Listed on the back, Earthworks | Haulage | Truck and Machinery Hire | Sand, Soil & Mulch Supply | Screening of Products
Nice to have
• Would be good for it to look appealing to a mans man, because it relates to heavy machinery, earthworks, construction etc. Black, red and white would be good maybe with a bit of silver somewhere.
Should not have
• not sure

```html
<!DOCTYPE html>
<html lang="en">
<head>
<meta charset="utf-8">
<title>BQL Groundworks &amp; Freight – Business Card</title>
<link rel="stylesheet" href="https://fonts.googleapis.com/css2?family=Tinos:wght@700&family=Roboto+Condensed:wght@400&family=Lato:wght@400&display=swap">
<style>
  :root {
    --red: #ec1f27;
    --red-deep: #8e1016;
    --black: #000000;
    --card: #0b0b0c;
    --card-edge: #17171a;
    --silver: #cbcbcb;
    --white: #ffffff;
    --stage: #2a2a2c;
    --text-soft: #c9c9cc;
  }
  * { box-sizing: border-box; margin: 0; padding: 0; }
  html, body { width: 1200px; height: 1200px; overflow: hidden; }
  body {
    background: var(--stage);
    display: flex;
    flex-direction: column;
    align-items: center;
    justify-content: center;
    gap: 60px;
  }
  .card {
    position: relative;
    width: 820px;
    height: 500px;
    background: radial-gradient(ellipse at 50% 40%, var(--card-edge) 0%, var(--card) 70%);
    box-shadow: 0 12px 30px rgba(0,0,0,.55);
    overflow: hidden;
  }
  .brand-mark {
    width: 26px; height: 26px;
    background: var(--silver);
    flex: none;
  }
  .brand-name {
    font-family: "Tinos", "Times New Roman", serif;
    font-weight: 700;
    letter-spacing: 1px;
    color: var(--silver);
    text-transform: uppercase;
    line-height: 1.08;
    white-space: nowrap;
  }

  /* Back */
  .card-back .brand {
    position: absolute;
    top: 120px;
    left: 0; right: 0;
    display: flex;
    align-items: center;
    justify-content: center;
    gap: 16px;
  }
  .card-back .brand-name { font-size: 38px; }
  .service-band {
    position: absolute;
    left: 0; right: 0;
    top: 345px;
    height: 50px;
    padding: 0 30px;
    background: linear-gradient(180deg, #8a8a8c 0%, var(--white) 35%, var(--silver) 70%, #5e5e60 100%);
    display: flex;
    align-items: center;
    justify-content: center;
    box-shadow: 0 10px 18px rgba(0,0,0,.6);
  }
  .service-list {
    font-family: "Roboto Condensed", Arial, sans-serif;
    font-size: 15px;
    color: var(--black);
    text-transform: uppercase;
    white-space: nowrap;
  }

  /* Front */
  .abn {
    position: absolute;
    top: 34px; right: 40px;
    font-family: "Roboto Condensed", Arial, sans-serif;
    font-size: 15px;
    color: var(--text-soft);
  }
  .card-front .brand {
    position: absolute;
    left: 50px;
    top: 195px;
    display: flex;
    align-items: center;
    gap: 14px;
  }
  .card-front .brand-mark { background: var(--red); width: 28px; height: 28px; }
  .card-front .brand-name { font-size: 27px; }
  .divider {
    position: absolute;
    left: 425px;
    top: 110px;
    width: 3px;
    height: 280px;
    background: linear-gradient(180deg, transparent 0%, var(--red) 30%, var(--red-deep) 75%, transparent 100%);
  }
  .contact {
    position: absolute;
    left: 470px;
    top: 160px;
  }
  .person-name {
    font-family: "Tinos", "Times New Roman", serif;
    font-weight: 700;
    font-size: 38px;
    color: var(--white);
    text-transform: uppercase;
    letter-spacing: 1px;
    white-space: nowrap;
  }
  .person-role {
    font-family: "Lato", Arial, sans-serif;
    font-size: 22px;
    color: var(--text-soft);
    margin-top: 2px;
  }
  .contact-list { list-style: none; margin-top: 44px; }
  .contact-item {
    display: flex;
    align-items: center;
    gap: 14px;
    font-family: "Lato", Arial, sans-serif;
    font-size: 21px;
    color: var(--white);
    margin-bottom: 10px;
    white-space: nowrap;
  }
  .contact-icon { width: 18px; height: 18px; flex: none; }
</style>
</head>
<body>

  <section class="card card-back" aria-label="Business card back">
    <div class="brand">
      <span class="brand-mark"></span>
      <span class="brand-name">BQL Groundworks<br>&amp; Freight</span>
    </div>
    <div class="service-band">
      <p class="service-list">Earthworks | Haulage | Truck and Machinery Hire | Sand, Soil &amp; Mulch Supply | Screening of Products</p>
    </div>
  </section>

  <section class="card card-front" aria-label="Business card front">
    <p class="abn">ABN 52 907 334 816</p>
    <div class="brand">
      <span class="brand-mark"></span>
      <span class="brand-name">BQL Groundworks<br>&amp; Freight</span>
    </div>
    <div class="divider"></div>
    <div class="contact">
      <h1 class="person-name">Doug Pelham</h1>
      <p class="person-role">Managing Director</p>
      <ul class="contact-list">
        <li class="contact-item">
          <svg class="contact-icon" viewBox="0 0 18 18" aria-hidden="true">
            <path d="M2 6 Q9 1 16 6 L14 8 L12 6.5 L6 6.5 L4 8 Z" fill="var(--red)"/>
            <rect x="4" y="9" width="10" height="7" rx="1" fill="var(--red)"/>
          </svg>
          <span>0438 256 904</span>
        </li>
        <li class="contact-item">
          <svg class="contact-icon" viewBox="0 0 18 18" aria-hidden="true">
            <rect x="1" y="4" width="16" height="11" fill="var(--red)"/>
            <path d="M1 4 L9 10 L17 4 M1 15 L7 9 M17 15 L11 9" stroke="var(--card)" stroke-width="1.2" fill="none"/>
          </svg>
          <span>bqlfreight2010@mailvane.net</span>
        </li>
      </ul>
    </div>
  </section>

</body>
</html>
```